Ridgeway Fruit Depot Logo/Label Design

I am designing a blueberry label that will be placed on clam shells when the fruit is packed. The label will the company name "The Ridgeway Fruit Depot". It will also list Blueberries/Bleuets (Blueberries in French). It small print it would say Dist. By/Par The Ridgeway Fruit Depot, Corliss, GA 30874 USA. It would also list the package size. 1 US Dry Pint/1 Chopine Seche US 551 ml. I have provided some sample labels that other marketers use.

```html
<!DOCTYPE html>
<html lang="en">
<head>
<meta charset="utf-8">
<title>The Ridgeway Fruit Depot – Pint Label</title>
<link rel="stylesheet" href="https://fonts.googleapis.com/css2?family=Titan+One&family=Barlow+Semi+Condensed:wght@300;500;600&display=swap">
<style>
  :root {
    --page: #ffffff;
    --sun: #fdc451;
    --teal: #1ec9a0;
    --teal-soft: #6fe3d2;
    --navy: #1c3557;
    --cream: #faf3e6;
    --berry-dark: #2f3d6a;
    --berry-mid: #4d6199;
    --berry-light: #7488bd;
  }
  html, body {
    margin: 0;
    width: 1200px;
    height: 800px;
    overflow: hidden;
    background: var(--page);
  }
  .label {
    position: absolute;
    left: 262px;
    top: 166px;
    width: 676px;
    height: 467px;
    display: block;
  }
  .brand-small,
  .brand-main {
    font-family: "Titan One", "Arial Black", sans-serif;
    font-weight: 900;
    fill: var(--cream);
  }
  .brand-small { font-size: 36px; }
  .brand-main { font-size: 84px; }
  .brand-french {
    font-family: "Titan One", "Arial Black", sans-serif;
    font-weight: 900;
    font-size: 31px;
    fill: var(--sun);
  }
  .product-name {
    font-family: "Titan One", "Arial Black", sans-serif;
    font-weight: 900;
    font-size: 31px;
    fill: var(--navy);
  }
  .pack-size {
    font-family: "Barlow Semi Condensed", "Arial Narrow", sans-serif;
    font-weight: 600;
    font-size: 25px;
    letter-spacing: -0.5px;
    fill: var(--navy);
  }
  .distributor {
    font-family: "Barlow Semi Condensed", "Arial Narrow", sans-serif;
    font-weight: 500;
    font-size: 21px;
    fill: var(--navy);
  }
  .barcode-frame {
    fill: none;
    stroke: var(--cream);
    stroke-width: 1.5;
  }
  .barcode-note {
    font-family: "Barlow Semi Condensed", "Arial Narrow", sans-serif;
    font-weight: 300;
    font-size: 44px;
    fill: var(--cream);
    opacity: 0.75;
  }
  .bullet { fill: var(--sun); }
</style>
</head>
<body>
<svg class="label" viewBox="0 0 844 584" xmlns="http://www.w3.org/2000/svg">
  <defs>
    <clipPath id="label-shape">
      <rect x="0" y="0" width="844" height="584" rx="20"/>
    </clipPath>
    <linearGradient id="berry-tones" x1="0" y1="0" x2="1" y2="1">
      <stop offset="0" stop-color="var(--berry-mid)"/>
      <stop offset="0.45" stop-color="var(--berry-light)"/>
      <stop offset="0.75" stop-color="var(--berry-mid)"/>
      <stop offset="1" stop-color="var(--berry-dark)"/>
    </linearGradient>
    <linearGradient id="size-band" x1="0" y1="0" x2="1" y2="0">
      <stop offset="0" stop-color="var(--teal-soft)"/>
      <stop offset="0.55" stop-color="var(--teal-soft)" stop-opacity="0.55"/>
      <stop offset="1" stop-color="var(--sun)" stop-opacity="0"/>
    </linearGradient>
    <path id="french-curve" d="M220 188 C 330 275, 470 345, 710 372"/>
  </defs>

  <g clip-path="url(#label-shape)">
    <rect class="berry-photo" x="0" y="0" width="844" height="420" fill="url(#berry-tones)"
          role="img" aria-label="Close-up photograph of fresh blueberries with water droplets"/>
    <path class="swoosh-shadow" d="M0 128 C 200 262, 450 398, 844 396 L844 410 C 450 410, 200 290, 0 160 Z" fill="var(--navy)"/>
    <path class="field" d="M0 155 C 200 280, 450 405, 844 402 L844 584 L0 584 Z" fill="var(--sun)"/>
    <path class="swoosh" d="M0 65 C 160 175, 420 385, 844 396 L844 402 C 440 405, 200 250, 0 128 Z" fill="var(--teal)"/>
    <rect class="size-band" x="0" y="397" width="320" height="63" fill="url(#size-band)"/>
  </g>

  <g class="brand">
    <text class="brand-small" x="152" y="102">The</text>
    <text class="brand-main" x="224" y="102" textLength="420" lengthAdjust="spacingAndGlyphs">Ridgeway</text>
    <text class="brand-main" x="300" y="188" textLength="470" lengthAdjust="spacingAndGlyphs">Fruit Depot</text>
    <text class="brand-french" textLength="500" lengthAdjust="spacingAndGlyphs"><textPath href="#french-curve">Le Dépôt Fruitier Ridgeway</textPath></text>
  </g>

  <g class="product">
    <text class="product-name" x="40" y="335">Blueberries</text>
    <text class="product-name" x="40" y="372">Bleuets</text>
  </g>

  <g class="pack-info">
    <circle class="bullet" cx="42" cy="416" r="6"/>
    <text class="pack-size" x="57" y="424">1 US Dry Pint</text>
    <circle class="bullet" cx="42" cy="445" r="6"/>
    <text class="pack-size" x="57" y="453">1 chopin sèche US 551 ml</text>
  </g>

  <g class="distributor-block">
    <text class="distributor" x="62" y="485">Dist. By/Par</text>
    <text class="distributor" x="62" y="510">The Ridgeway Fruit Depot,</text>
    <text class="distributor" x="62" y="535">Corliss, GA 30874 USA</text>
  </g>

  <g class="barcode-area">
    <rect class="barcode-frame" x="519" y="423" width="280" height="138" rx="5"/>
    <text class="barcode-note" x="659" y="508" text-anchor="middle">BARCODE</text>
  </g>
</svg>
</body>
</html>
```